Accounting & Tax Services in Edmonton, Canada-Needs Website Design & Improvement

I am starting my business for accounting and tax services in Canada. I have my website but not much happy with that. My services are for bookkeeping, accounting and tax services. We serve both individual and corporate clients. I am trying to bring new idea in the market for providing services at their facility or business. My existing website is www.qrmt.ca
Currently, this site is static but I want to improve it to dynamic or interactive in nature.

Target Market(s)

Edmonton and Surrounding Areas, Canada

Industry/Entity Type

Public Accounting

Logo Text

Harborline Ledger & Advisory Partners

Number of Pages Required

4 page

Font styles to use
Sans Serif

Colors

Designer to choose colors to be used in the design.

Requirements
Must have
• 4 Pages
• I a not sure what do we mean by coded and uncoded design. Need clarification
• Rest is explained in project description. It should have the ingredients to attract traffic in any professional website.
• Logo Design Text can be shortened, if required.
• Existing logo attached, just for reference.
Nice to have
• 5 Pages

```html
<!DOCTYPE html>
<html lang="en">
<head>
<meta charset="utf-8">
<title>Harborline Ledger – Accounting &amp; Tax Services</title>
<link href="https://fonts.googleapis.com/css2?family=Noto+Serif:wght@400;700&family=Open+Sans:wght@400;600&display=swap" rel="stylesheet">
<style>
:root{
  --teal-dark:#1f5673;
  --teal:#2e6b86;
  --teal-light:#5aa1b3;
  --ink:#333;
  --muted:#555;
  --line:#ddd;
  --dark-bar:#2f2f2f;
  --accent-red:#d8262e;
  --white:#fff;
  --serif:"Noto Serif", Georgia, serif;
  --sans:"Open Sans", Arial, sans-serif;
}
*{box-sizing:border-box;margin:0;padding:0}
html,body{width:1200px;height:3333px;overflow:hidden}
body{font-family:var(--sans);color:var(--ink);background:var(--white);position:relative}
.abs{position:absolute}
section,header,footer{position:absolute;left:0;width:1200px}

/* header */
.site-header{top:0;height:125px;border-top:4px solid var(--accent-red);background:var(--white)}
.brand{left:76px;top:22px;text-align:center;width:225px}
.brand-name{font-family:var(--serif);font-size:23px;color:var(--teal-dark);line-height:1.2}
.brand-sub{font-family:var(--serif);font-size:15px;color:var(--teal-dark)}
.brand-dot{width:14px;height:14px;border-radius:50%;background:var(--teal);margin:0 auto 12px}
.call{right:78px;top:14px;display:flex;align-items:center;gap:12px;font-size:15px;color:var(--muted)}
.call-icon{width:40px;height:40px;border:1.5px solid #999;border-radius:50%;display:flex;align-items:center;justify-content:center}
.call b{font-size:21px;color:var(--teal-dark)}
.main-nav{right:78px;top:80px;display:flex;gap:33px;font-size:16px;color:var(--muted)}
.main-nav .active{color:var(--teal)}

/* hero */
.hero{top:125px;height:595px;background:linear-gradient(100deg,#eef1f3 0%,#d7dde2 45%,#9aa7b0 70%,#c8ced3 100%)}
.hero-title{left:76px;top:215px;font-family:var(--serif);font-weight:400;font-size:46px;color:var(--teal-dark)}
.hero-sub{left:78px;top:280px;font-family:var(--serif);font-size:28px;color:#444}
.btn{display:inline-flex;align-items:center;justify-content:center;font-family:var(--serif);font-size:17px;text-transform:uppercase;height:44px}
.btn-solid{left:76px;top:333px;width:190px;background:var(--teal-dark);color:var(--white)}
.btn-outline{left:274px;top:333px;width:190px;border:2px solid var(--teal-dark);color:var(--teal-dark);background:rgba(255,255,255,.4)}
.hero-arrow{top:270px;font-size:34px;color:#555}

/* services */
.services{top:720px;height:428px}
.service{top:80px;width:240px;height:282px}
.service-label{height:95px;background:#e6e6e6;display:flex;flex-direction:column;align-items:center;justify-content:flex-end;padding-bottom:10px;font-family:var(--serif);font-size:19px;color:var(--teal-dark)}
.service-label i{width:30px;height:30px;background:var(--teal);margin-bottom:8px;display:block}
.service-photo{height:187px}

/* welcome */
.welcome{top:1148px;height:310px;background:linear-gradient(90deg,var(--teal-dark),var(--teal-light));color:var(--white);text-align:center}
.welcome h2{font-family:var(--serif);font-weight:400;font-size:37px;margin-top:44px}
.welcome p{width:880px;margin:14px auto 0;font-size:14px;line-height:1.7}

/* growth */
.growth{top:1458px;height:418px;text-align:center}
.growth h2{font-family:var(--serif);font-weight:400;font-size:31px;color:var(--teal-dark);margin-top:42px}
.growth p{width:740px;margin:14px auto 0;font-size:14px;line-height:1.7;color:var(--muted)}
.stat{top:178px;width:128px;height:180px}
.stat::before,.stat::after{content:"";position:absolute;left:0;right:0;height:34px;border:2px solid var(--teal-dark)}
.stat::before{top:0;border-bottom:none}
.stat::after{bottom:0;border-top:none}
.stat-num{position:absolute;left:-60px;right:-60px;top:38px;font-family:var(--serif);font-size:56px;color:var(--teal-dark)}
.stat-label{position:absolute;left:-60px;right:-60px;top:114px;font-size:18px;color:var(--muted)}

/* tax alerts */
.alerts{top:1876px;height:312px;background:linear-gradient(90deg,#f2f2f2,#dcdcdc 60%,#c9c9c9)}
.alerts h2{position:absolute;left:0;right:0;top:42px;text-align:center;font-family:var(--serif);font-weight:400;font-size:35px;color:var(--teal-dark)}
.alert{top:120px;width:476px}
.alert h3{font-family:var(--serif);font-weight:400;font-size:20px;color:#222;line-height:1.35}
.alert p{font-size:13.5px;line-height:1.8;color:#333;margin-top:4px}
.dots{left:556px;top:268px;display:flex;gap:5px}
.dots span{width:14px;height:14px;border-radius:50%;border:2px solid var(--teal-dark)}
.dots .on{background:var(--teal-dark)}

/* quote */
.quote{top:2188px;height:312px;background:linear-gradient(90deg,var(--teal-dark),var(--teal-light))}
.quote h2{left:182px;top:80px;font-family:var(--serif);font-weight:400;font-size:35px;color:var(--white)}
.quote p{left:216px;top:145px;width:342px;text-align:right;font-size:15px;line-height:1.7;color:var(--white)}
.field{height:46px;background:rgba(255,255,255,.3);color:var(--white);font-size:14px;padding:13px 14px}
.submit{left:585px;top:202px;width:166px;height:50px;background:#2b2e32;color:var(--white);font-family:var(--serif);font-size:17px;display:flex;align-items:center;justify-content:center}

/* blog */
.blog{top:2500px;height:415px}
.blog h2{position:absolute;left:0;right:0;top:42px;text-align:center;font-family:var(--serif);font-weight:400;font-size:35px;color:var(--teal-dark)}
.post{top:105px;width:470px;height:230px;border:1px solid var(--line);display:flex}
.post-photo{width:208px;height:100%;position:relative}
.post-date{position:absolute;width:64px;height:78px;background:var(--teal-dark);color:var(--white);text-align:center;font-family:var(--serif)}
.post-date b{display:block;font-weight:400;font-size:30px;line-height:46px}
.post-date span{font-size:14px}
.post-body{padding:28px 20px 0 24px;flex:1}
.post-body h3{font-family:var(--serif);font-weight:400;font-size:18px;line-height:1.45;color:#222}
.post-body p{font-size:13.5px;line-height:1.8;color:var(--muted);margin-top:10px}

/* signup */
.signup{top:2915px;height:105px;background:var(--dark-bar)}
.signup h2{left:78px;top:35px;font-family:var(--serif);font-weight:400;font-size:25px;color:var(--white)}
.signup-input{left:690px;top:36px;width:296px;height:41px;background:var(--white);font-size:14px;color:#444;padding:11px 12px}
.signup-btn{left:996px;top:36px;width:126px;height:41px;background:var(--teal);color:var(--white);font-family:var(--serif);font-size:16px;display:flex;align-items:center;justify-content:center}

/* footer */
.site-footer{top:3020px;height:313px;background:linear-gradient(90deg,var(--teal-dark),var(--teal-light));color:var(--white)}
.footer-brand{left:76px;top:94px;width:270px;text-align:center}
.footer-brand .brand-dot{background:var(--white);width:20px;height:20px;margin-bottom:10px}
.footer-brand .name{font-family:var(--serif);font-size:29px;line-height:1.25}
.footer-brand .sub{font-family:var(--serif);font-size:19px}
.contact{left:844px;top:48px;width:266px;font-size:13.5px;line-height:1.8}
.contact li{list-style:none;display:flex;gap:14px;margin-bottom:6px}
.contact svg{flex:none;margin-top:3px}
.footer-rule{left:0;top:250px;width:1200px;height:1px;background:rgba(255,255,255,.25)}
.copyright{left:0;right:0;top:272px;text-align:center;font-size:14px}
</style>
</head>
<body>

<header class="site-header">
  <div class="abs brand">
    <div class="brand-dot"></div>
    <div class="brand-name">Harborline Ledger</div>
    <div class="brand-sub">Advisory Partners</div>
  </div>
  <div class="abs call">
    <span class="call-icon"><svg width="18" height="18" viewBox="0 0 24 24"><path d="M6.6 10.8a15 15 0 0 0 6.6 6.6l2.2-2.2c.3-.3.7-.4 1-.2 1.1.4 2.3.6 3.6.6.6 0 1 .4 1 1V20c0 .6-.4 1-1 1A17 17 0 0 1 3 4c0-.6.4-1 1-1h3.5c.6 0 1 .4 1 1 0 1.300.2 2.5.6 3.6.1.3 0 .7-.2 1z" fill="#555"/></svg></span>
    <span>Call Us Now : <b>555-0142-318</b></span>
  </div>
  <nav class="abs main-nav">
    <span class="active">Home</span><span>About Us</span><span>Services</span><span>Newsletter</span><span>Financial Tools</span><span>Info Center</span><span>Contact</span>
  </nav>
</header>

<section class="hero" role="img" aria-label="Photo of two smiling colleagues reviewing a tablet at an office desk">
  <div class="abs hero-arrow" style="left:30px">&#x2039;</div>
  <div class="abs hero-arrow" style="right:30px">&#x203A;</div>
  <h1 class="abs hero-title">Harborline Ledger</h1>
  <div class="abs hero-sub">Your Success is our Business</div>
  <div class="abs btn btn-solid">Client Portal</div>
  <div class="abs btn btn-outline">Know More</div>
</section>

<section class="services">
  <div class="abs service" style="left:160px">
    <div class="service-label"><i></i>Bookkeeping</div>
    <div class="service-photo" role="img" aria-label="Photo of a calculator, notebook and coffee cup on a ledger sheet" style="background:linear-gradient(135deg,#d9d2c4,#b9ae97 50%,#e8d98a)"></div>
  </div>
  <div class="abs service" style="left:480px">
    <div class="service-label"><i></i>Accounting</div>
    <div class="service-photo" role="img" aria-label="Photo of financial charts, a laptop and a calculator on a desk" style="background:linear-gradient(135deg,#6f8fb5,#c9d3dc 50%,#e7b96a)"></div>
  </div>
  <div class="abs service" style="left:800px">
    <div class="service-label"><i></i>Tax services</div>
    <div class="service-photo" role="img" aria-label="Photo of a tax form with a pen and a calculator" style="background:linear-gradient(135deg,#e9e9e9,#b5bcc5 55%,#7d8794)"></div>
  </div>
</section>

<section class="welcome">
  <h2>Welcome To Harborline Ledger</h2>
  <p>Welcome and thank you for visiting our website. At Harborline Ledger &amp; Advisory Partners, we have built our business so that it guarantees your success. In addition to providing you with a profile of our firm and the services we provide, this website has been designed to become a helpful resource tool to you, our valued clients and visitors.</p>
  <p>Our firm endeavors to provide you with the highest quality of service and we hope that you find the information on this website useful. For any additional questions or comments please do not hesitate to contact us. We will get back to you as soon as possible as we pride ourselves on being proactive and responsive to our clients' inquiries and suggestions.</p>
</section>

<section class="growth">
  <h2>We are help you to grow your business</h2>
  <p>At Harborline Ledger &amp; Advisory Partners, we work hard to realize our motto. We view every client relationship like a partnership, and truly believe that our success is a result of your success.</p>
  <div class="abs stat" style="left:172px"><div class="stat-num">10</div><div class="stat-label">Years of experience</div></div>
  <div class="abs stat" style="left:535px"><div class="stat-num">1120</div><div class="stat-label">Happy Customers</div></div>
  <div class="abs stat" style="left:898px"><div class="stat-num">100%</div><div class="stat-label">Satisfaction</div></div>
</section>

<section class="alerts" role="img" aria-label="Soft photo of a hand using a calculator beside a keyboard">
  <h2>Tax Alerts</h2>
  <article class="abs alert" style="left:80px">
    <h3>AB - Interest Rates - 2017</h3>
    <p>The province of Alberta levies and pays interest on underpayments and overpayments of tax at rates prescribed by statute and set at the beginning of each calendar quarter. The rates to be levied and p...</p>
  </article>
  <article class="abs alert" style="left:640px">
    <h3>AB - Provincial film and television grant program expanded</h3>
    <p>The government of Alberta has announced changes to its incentive programs for Alberta-based film and television productions...</p>
  </article>
  <div class="abs dots"><span></span><span></span><span></span><span class="on"></span></div>
</section>

<section class="quote">
  <h2 class="abs">Request A Free Quote</h2>
  <p class="abs">Please feel free to contact us at the information provided below and we will be sure to get back to you as soon as possible.</p>
  <div class="abs field" style="left:585px;top:80px;width:249px">Name</div>
  <div class="abs field" style="left:845px;top:80px;width:249px">Email</div>
  <div class="abs field" style="left:585px;top:140px;width:509px">Subject</div>
  <div class="abs submit">SUBMIT</div>
</section>

<section class="blog">
  <h2>Latest Blog</h2>
  <article class="abs post" style="left:98px">
    <div class="post-photo" role="img" aria-label="Photo of a woman working on a laptop" style="background:linear-gradient(135deg,#8a7560,#d7cbbb 60%,#efe9e1)">
      <div class="post-date" style="right:0;top:34px"><b>29</b><span>APR</span></div>
    </div>
    <div class="post-body"><h3>Lorem Ipsum is simply dummy text.</h3><p>Lorem Ipsum is simply dummy text of the printing and typesetting industry. Lorem Ipsum has been the industry's standard dummy text.</p></div>
  </article>
  <article class="abs post" style="left:634px">
    <div class="post-photo" role="img" aria-label="Photo of hands holding a smartphone" style="background:linear-gradient(135deg,#c8d6df,#8fa6b5 55%,#5e7383)">
      <div class="post-date" style="right:0;bottom:33px"><b>29</b><span>APR</span></div>
    </div>
    <div class="post-body"><h3>Lorem Ipsum is simply dummy text.</h3><p>Lorem Ipsum is simply dummy text of the printing and typesetting industry. Lorem Ipsum has been the industry's standard dummy text.</p></div>
  </article>
</section>

<section class="signup">
  <h2 class="abs">To get latest updates and promotions signup now!</h2>
  <div class="abs signup-input">Enter Your Email</div>
  <div class="abs signup-btn">SUBSCRIBE</div>
</section>

<footer class="site-footer">
  <div class="abs footer-brand">
    <div class="brand-dot"></div>
    <div class="name">Harborline Ledger</div>
    <div class="sub">Advisory Partners</div>
  </div>
  <ul class="abs contact">
    <li><svg width="16" height="20" viewBox="0 0 16 20"><path d="M8 0a7 7 0 0 0-7 7c0 5 7 13 7 13s7-8 7-13a7 7 0 0 0-7-7zm0 10a3 3 0 1 1 0-6 3 3 0 0 1 0 6z" fill="#fff"/></svg><span>Riverbend Commons Suite 410-8820 104 Ave NW Edmonton, AB T5J 0K3</span></li>
    <li><svg width="16" height="16" viewBox="0 0 24 24"><path d="M6.6 10.8a15 15 0 0 0 6.6 6.6l2.2-2.2c.3-.3.7-.4 1-.2 1.1.4 2.3.6 3.6.6.6 0 1 .4 1 1V20c0 .6-.4 1-1 1A17 17 0 0 1 3 4c0-.6.4-1 1-1h3.5c.6 0 1 .4 1 1 0 1.3.2 2.5.6 3.6.1.3 0 .7-.2 1z" fill="#fff"/></svg><span>Main Office: (587) 555 0148</span></li>
    <li><svg width="16" height="16" viewBox="0 0 24 24"><path d="M6.6 10.8a15 15 0 0 0 6.6 6.6l2.2-2.2c.3-.3.7-.4 1-.2 1.1.4 2.3.6 3.6.6.6 0 1 .4 1 1V20c0 .6-.4 1-1 1A17 17 0 0 1 3 4c0-.6.4-1 1-1h3.5c.6 0 1 .4 1 1 0 1.3.2 2.5.6 3.6.1.3 0 .7-.2 1z" fill="#fff"/></svg><span>Accounting Direct: (587) 555 0193</span></li>
    <li><svg width="16" height="14" viewBox="0 0 16 12"><rect x=".75" y=".75" width="14.5" height="10.5" fill="none" stroke="#fff" stroke-width="1.5"/><path d="M1 1l7 6 7-6" fill="none" stroke="#fff" stroke-width="1.5"/></svg><span>hello@harborlineledger-demo.ca</span></li>
  </ul>
  <div class="abs footer-rule"></div>
  <div class="abs copyright">©Harborline Ledger - 2017. All Rights Reserved.</div>
</footer>

</body>
</html>
```